Wren Vehicle Polishing (Mobile detail)

I need a business card made up. I'd like it to be different in some form, either raised, embossed, debossed, something cool that stands out. (preferably embossed text somewhere in it). I will be including the Initial png file. Let me know if you need the photoshop of adobe illustrator file to work with.

Information to be included: Text: XXX-XXX-XXXX Phone: XXX-XXX-XXXX Email: wrenpolishcrew@mailbox-demo.net Website: www.socialpage-demo.net/wrenpolishKTR Hours of operation: Mon - Fri 7:00AM to 8:00PM Sat - 10:00AM to 8:00PM

Target Market(s)

Mobile automotive detailing

Industry/Entity Type

Automotive

Contact Information for Business Card

Make it stand out with embossed lettering, I'd also like the background to be glossy black or matte, something that represents a shiny car, black preferred

Requirements
Must have
• A glossy background, or something.
• My logo, pick one of them that best fits your design.
Should not have
• White background,
• something that does not stand out.

```html
<!DOCTYPE html>
<html lang="en">
<head>
<meta charset="utf-8">
<title>Wren Vehicle Polishing — Business Card</title>
<link rel="stylesheet" href="https://fonts.googleapis.com/css2?family=Open+Sans:wght@400;600;700&display=swap">
<style>
  :root {
    --stage: #cfcfcf;
    --card-top: #2b2b2b;
    --card-mid: #1c1c1c;
    --card-bottom: #121212;
    --ink: #ffffff;
    --ink-soft: #e6e6e6;
    --rule: #9a9a9a;
    --accent: #f26a21;
  }
  * { margin: 0; padding: 0; box-sizing: border-box; }
  html, body {
    width: 1200px;
    height: 1000px;
    overflow: hidden;
  }
  body {
    background: var(--stage);
    font-family: "Open Sans", Arial, sans-serif;
    display: flex;
    align-items: center;
    justify-content: center;
  }
  .business-card {
    position: relative;
    width: 900px;
    height: 514px;
    background:
      radial-gradient(ellipse 70% 55% at 50% 30%, rgba(255,255,255,0.08), rgba(255,255,255,0) 70%),
      linear-gradient(170deg, var(--card-top) 0%, var(--card-mid) 55%, var(--card-bottom) 100%);
    box-shadow: 0 18px 40px rgba(0,0,0,0.35);
    color: var(--ink);
  }
  .brand {
    position: absolute;
    top: 92px;
    left: 0;
    right: 0;
    display: flex;
    align-items: center;
    justify-content: center;
    gap: 16px;
  }
  .brand-dot {
    width: 34px;
    height: 34px;
    border-radius: 50%;
    background: var(--accent);
  }
  .brand-name {
    font-size: 40px;
    font-weight: 700;
    color: var(--ink);
    letter-spacing: 0.5px;
  }
  .contact-row {
    position: absolute;
    top: 300px;
    left: 0;
    right: 0;
    display: flex;
    justify-content: center;
  }
  .person {
    text-align: right;
    padding-right: 18px;
    padding-top: 8px;
  }
  .person-name {
    font-size: 27px;
    font-weight: 600;
    letter-spacing: 0.3px;
    line-height: 1.15;
  }
  .person-role {
    font-size: 19px;
    font-weight: 600;
    color: var(--ink-soft);
    letter-spacing: 0.5px;
  }
  .divider {
    width: 1px;
    height: 80px;
    background: var(--rule);
  }
  .details {
    list-style: none;
    padding-left: 18px;
    font-size: 20px;
    font-weight: 600;
    line-height: 1.3;
  }
  .hours {
    position: absolute;
    top: 410px;
    left: 0;
    right: 0;
    text-align: center;
    font-size: 22px;
    font-weight: 600;
    line-height: 1.3;
  }
  .hours-sep { padding: 0 10px; }
</style>
</head>
<body>
  <article class="business-card">
    <header class="brand">
      <span class="brand-dot" aria-hidden="true"></span>
      <span class="brand-name">Wren Vehicle Polishing</span>
    </header>

    <section class="contact-row">
      <div class="person">
        <p class="person-name">PERSON NAME</p>
        <p class="person-role">DESIGNATION</p>
      </div>
      <div class="divider" aria-hidden="true"></div>
      <ul class="details">
        <li>P: 123 456 7890</li>
        <li>F: 123 456 7890</li>
        <li>E: wrenpolishcrew@mailbox-demo.net</li>
      </ul>
    </section>

    <section class="hours">
      <p>Hours of operation:</p>
      <p>Mon - Fri 7:00AM to 8:00PM<span class="hours-sep">|</span>Sat - 10:00AM to 8:00PM</p>
    </section>
  </article>
</body>
</html>
```